Assessment Flyer

We are looking for a marketing flyer for our business. We are a psychology practice that has recently expanded our assessment team and availability. We need a flyer to fax to GP's and other referrers. We have previously sent out rather basic flyers as it was more of a courtesy update about our practice rather than a marketing tool. We have recently created a brochure just focusing on assessments which can be used as a guide for the flyer. We want to update them about our expansion, highlight the assessments we do, introduce our new psychologists, and touch on availability.

```html
<!DOCTYPE html>
<html lang="en">
<head>
<meta charset="utf-8">
<title>Assessment Service Flyer</title>
<link rel="stylesheet" href="https://fonts.googleapis.com/css2?family=Playfair+Display:wght@800;900&family=Poppins:wght@400;500;600;700&family=Oswald:wght@500&display=swap">
<style>
:root{
  --teal:#3f9f8d;
  --teal-dark:#2f8a79;
  --green:#5cb85f;
  --mint:#cbe5d9;
  --ink:#121212;
  --paper:#ffffff;
  --backdrop:#8a8f8d;
  --photo-dark:#2a2412;
  --photo-mid:#6b5a22;
  --photo-light:#d9b23a;
}
*{margin:0;padding:0;box-sizing:border-box}
html,body{width:1200px;height:2386px;overflow:hidden}
body{background:var(--backdrop);font-family:'Poppins',sans-serif;color:var(--ink);position:relative}
.flyer{position:absolute;left:50px;top:480px;width:1100px;height:1426px;background:var(--paper);overflow:hidden;box-shadow:0 12px 30px rgba(0,0,0,.35)}
.hero{position:absolute;left:0;top:0;width:1100px;height:500px;background:radial-gradient(circle at 68% 30%,#f1d77a 0%,var(--photo-light) 14%,var(--photo-mid) 45%,var(--photo-dark) 100%)}
.hero-edge{position:absolute;left:0;top:380px;width:1100px;height:125px}
.brand{position:absolute;left:70px;top:290px;display:flex;align-items:center;gap:12px;font-family:'Poppins',sans-serif;font-weight:600;font-size:26px;color:var(--teal);line-height:1.15}
.brand-dot{width:22px;height:22px;border-radius:50%;background:var(--teal);flex:none}
.title{position:absolute;left:52px;top:528px;width:505px;font-family:'Playfair Display',serif;font-weight:900;line-height:.9;white-space:nowrap}
.title-top{display:block;font-size:73px;color:var(--ink);letter-spacing:-1.5px}
.title-main{display:block;font-size:112px;color:var(--teal);letter-spacing:-3px;margin-top:4px}
.title-rule{position:absolute;left:582px;top:530px;width:2px;height:172px;background:var(--teal)}
.intro{position:absolute;left:604px;top:528px;width:450px;font-size:21px;line-height:1.2;font-weight:500}
.intro strong{color:var(--teal);font-weight:600}
.pill-label{position:absolute;left:50px;top:733px;height:39px;padding:0 16px 0 18px;background:var(--green);color:#fff;font-weight:600;font-size:23px;letter-spacing:.5px;line-height:39px;border-radius:0 20px 20px 0;border-left:5px solid var(--teal-dark)}
.pill-label::before{content:"";position:absolute;left:-11px;top:0;width:3px;height:39px;background:var(--green)}
.assessments{position:absolute;left:50px;top:793px;width:997px;height:104px;display:flex}
.assess{display:flex;align-items:center;gap:12px;padding:0 12px;color:#fff;font-size:18px;line-height:1.2;font-weight:500}
.assess:nth-child(even){background:var(--mint);color:var(--ink)}
.assess:nth-child(odd){background:var(--teal)}
.assess b{font-weight:600}
.assess-icon{width:50px;height:50px;border-radius:50%;border:3px solid #fff;background:var(--teal);flex:none;display:flex;align-items:center;justify-content:center}
.team-heading{position:absolute;left:50px;top:936px;font-weight:700;font-size:39px;letter-spacing:-.5px;display:flex;align-items:center;width:997px}
.team-heading span{color:var(--teal);margin-left:12px}
.team-heading::after{content:"";flex:1;height:2px;background:var(--teal);margin:18px 0 0 6px}
.member{position:absolute;height:50px;background:var(--mint);border-radius:4px;box-shadow:0 2px 3px rgba(0,0,0,.18);padding:5px 0 0 68px}
.member-photo{position:absolute;left:0;top:-6px;width:58px;height:58px;border-radius:50%;background:radial-gradient(circle at 50% 40%,#c99d80,#6b4a3a);border:3px solid #fff}
.member-name{font-weight:600;font-size:16.5px;line-height:1.2;text-transform:uppercase;white-space:nowrap}
.member-role{font-size:14px;line-height:1.3;white-space:nowrap}
.col-a{left:50px;width:290px}
.col-b{left:357px;width:345px}
.availability{position:absolute;left:738px;top:1001px;width:310px}
.availability h3{font-weight:700;font-size:41px;color:var(--green);letter-spacing:1.5px;line-height:1}
.availability p{font-weight:600;font-size:28px;line-height:1.05;margin-top:14px}
.date-box{position:absolute;left:738px;top:1133px;width:310px;height:90px;display:flex;border:3px solid var(--teal)}
.date-month{width:152px;background:#fff;font-weight:700;font-size:32px;line-height:.95;padding:10px 0 0 12px}
.date-year{flex:1;background:var(--green);color:#fff;font-family:'Oswald',sans-serif;font-weight:500;font-size:70px;line-height:84px;text-align:center}
.contact-tab{position:absolute;left:210px;top:1268px;width:680px;height:48px}
.contact-tab-label{position:absolute;left:250px;top:1270px;width:600px;height:46px;background:var(--green);color:#fff;font-weight:600;font-size:27px;text-align:center;line-height:46px;letter-spacing:.5px}
.footer{position:absolute;left:0;top:1290px;width:1100px;height:136px;background:var(--teal);color:#fff;font-size:16.5px;font-weight:500}
.footer-col{position:absolute;top:50px;line-height:1.6}
.footer-line{display:flex;align-items:center;gap:5px;white-space:nowrap}
.footer-sep{position:absolute;top:48px;width:1px;height:54px;background:#fff}
</style>
</head>
<body>
<main class="flyer">
  <div class="hero" role="img" aria-label="Photo of a woman silhouetted sitting cross-legged on a hilltop against a golden sunset"></div>
  <svg class="hero-edge" viewBox="0 0 1100 125" preserveAspectRatio="none" aria-hidden="true">
    <path d="M0 40 L40 55 L90 48 L140 66 L200 58 L260 74 L320 80 L380 70 L440 84 L500 78 L560 96 L620 102 L660 112 L700 92 L760 60 L820 48 L880 40 L940 28 L1000 34 L1060 22 L1100 30 L1100 125 L0 125 Z" fill="#fff"/>
  </svg>
  <div class="brand"><span class="brand-dot"></span><span>Harbourline<br>Psychology &amp; Wellness</span></div>

  <h1 class="title"><span class="title-top">ASSESSMENT</span><span class="title-main">SERVICE</span></h1>
  <div class="title-rule"></div>
  <p class="intro"><strong>Harbourline Psychology &amp; Wellness is</strong> excited to announce the expansion of our assessment team. As the need for assessment services has grown, we have worked diligently to expand our team with highly skilled psychologists to support these needs.</p>

  <div class="pill-label">AVAILABLE ASSESSMENTS</div>
  <div class="assessments">
    <div class="assess" style="width:210px"><span class="assess-icon"><svg width="24" height="24" viewBox="0 0 24 24"><circle cx="12" cy="12" r="8" fill="none" stroke="#fff" stroke-width="2.5"/><circle cx="12" cy="12" r="3" fill="#fff"/></svg></span><span>Educational<br>Assessment</span></div>
    <div class="assess" style="width:193px"><span class="assess-icon"><svg width="24" height="24" viewBox="0 0 24 24"><path d="M12 3a7 7 0 0 0-4 12.7V19h8v-3.3A7 7 0 0 0 12 3z" fill="none" stroke="#fff" stroke-width="2.2"/><rect x="9" y="20" width="6" height="2" fill="#fff"/></svg></span><span><b>Intellectual<br>Disability</b></span></div>
    <div class="assess" style="width:212px"><span class="assess-icon"><svg width="24" height="24" viewBox="0 0 24 24"><circle cx="12" cy="5" r="2.6" fill="#fff"/><path d="M8 10h8v6h-2v6h-4v-6H8z" fill="#fff"/></svg></span><span><b>ADHD:</b><br>Children and<br>Adults</span></div>
    <div class="assess" style="width:193px"><span class="assess-icon"><svg width="24" height="24" viewBox="0 0 24 24"><circle cx="9" cy="5" r="2.4" fill="#fff"/><path d="M6 9h6v6h-1.5v7h-3v-7H6z" fill="#fff"/><circle cx="16.5" cy="11" r="1.8" fill="#fff"/><path d="M14.5 14h4v4h-1v4h-2v-4h-1z" fill="#fff"/></svg></span><span><b>Autism:</b><br>Children<br>and Adults</span></div>
    <div class="assess" style="width:189px"><span class="assess-icon"><svg width="24" height="24" viewBox="0 0 24 24"><rect x="4" y="10" width="16" height="11" fill="none" stroke="#fff" stroke-width="2.2"/><rect x="3" y="7" width="18" height="4" fill="#fff"/><rect x="11" y="7" width="2" height="14" fill="#fff"/></svg></span><span><b>Giftedness</b></span></div>
  </div>

  <h2 class="team-heading">MEET THE<span>ASSESSMENT TEAM</span></h2>

  <div class="member col-a" style="top:1000px"><div class="member-photo" role="img" aria-label="Portrait of Dr Maren Holt"></div><div class="member-name">Dr Maren Holt</div><div class="member-role">Clinical Director</div></div>
  <div class="member col-a" style="top:1062px"><div class="member-photo" role="img" aria-label="Portrait of Dr Elsa Brandt"></div><div class="member-name">Dr Elsa Brandt</div><div class="member-role">Registered Psychologist</div></div>
  <div class="member col-a" style="top:1124px"><div class="member-photo" role="img" aria-label="Portrait of Dr Nina Okafor"></div><div class="member-name">Dr Nina Okafor</div><div class="member-role">Counselling Psychologist</div></div>
  <div class="member col-a" style="top:1186px"><div class="member-photo" role="img" aria-label="Portrait of Clara Vensel"></div><div class="member-name">Clara Vensel</div><div class="member-role">Registered Psychologist</div></div>

  <div class="member col-b" style="top:1000px"><div class="member-photo" role="img" aria-label="Portrait of Talia Moreno"></div><div class="member-name">Talia Moreno</div><div class="member-role">Registered Psychologist</div></div>
  <div class="member col-b" style="top:1062px"><div class="member-photo" role="img" aria-label="Portrait of Rosalind Ashby Kerr"></div><div class="member-name">Rosalind Ashby Kerr</div><div class="member-role">Registered Psychologist</div></div>
  <div class="member col-b" style="top:1124px"><div class="member-photo" role="img" aria-label="Portrait of Hannah Ellery"></div><div class="member-name">Hannah Ellery</div><div class="member-role">Provisional Psychologist</div></div>
  <div class="member col-b" style="top:1186px"><div class="member-photo" role="img" aria-label="Portrait of Jess Whitford"></div><div class="member-name">Jess Whitford</div><div class="member-role">Provisional Psychologist</div></div>

  <div class="availability"><h3>AVAILABILITY</h3><p>APPOINTMENTS<br>AVAILABLE FROM</p></div>
  <div class="date-box"><div class="date-month">EARLY<br>MARCH</div><div class="date-year">2024</div></div>

  <footer class="footer">
    <div class="footer-col" style="left:55px">
      <div class="footer-line"><svg width="13" height="13" viewBox="0 0 24 24"><path d="M6 2l4 5-2 3a12 12 0 0 0 6 6l3-2 5 4-3 4C10 22 2 14 2 5z" fill="none" stroke="#fff" stroke-width="2"/></svg>08 7000 1234</div>
      <div class="footer-line"><svg width="13" height="13" viewBox="0 0 24 24"><path d="M6 2l4 5-2 3a12 12 0 0 0 6 6l3-2 5 4-3 4C10 22 2 14 2 5z" fill="none" stroke="#fff" stroke-width="2"/></svg>08 7000 5678</div>
    </div>
    <div class="footer-sep" style="left:200px"></div>
    <div class="footer-col" style="left:218px">
      <div class="footer-line"><svg width="14" height="12" viewBox="0 0 24 18"><rect x="1" y="1" width="22" height="16" fill="none" stroke="#fff" stroke-width="2"/><path d="M1 1l11 9 11-9" fill="none" stroke="#fff" stroke-width="2"/></svg>reception@harbourlinewellness.com.au</div>
      <div class="footer-line"><svg width="13" height="13" viewBox="0 0 24 24"><circle cx="12" cy="12" r="10" fill="none" stroke="#fff" stroke-width="2"/><path d="M2 12h20M12 2c4 5 4 15 0 20M12 2c-4 5-4 15 0 20" fill="none" stroke="#fff" stroke-width="1.6"/></svg>www.harbourlinewellness.com.au</div>
    </div>
    <div class="footer-sep" style="left:640px"></div>
    <div class="footer-col" style="left:655px">
      <div class="footer-line"><svg width="12" height="14" viewBox="0 0 20 24"><path d="M10 1a8 8 0 0 0-8 8c0 6 8 14 8 14s8-8 8-14a8 8 0 0 0-8-8z" fill="none" stroke="#fff" stroke-width="2"/><circle cx="10" cy="9" r="3" fill="#fff"/></svg>14 Shoreline Road, Seacliff Bay, SA 5099</div>
      <div class="footer-line"><svg width="12" height="14" viewBox="0 0 20 24"><path d="M10 1a8 8 0 0 0-8 8c0 6 8 14 8 14s8-8 8-14a8 8 0 0 0-8-8z" fill="none" stroke="#fff" stroke-width="2"/><circle cx="10" cy="9" r="3" fill="#fff"/></svg>2/40 Tidewater Terrace, Seacliff Bay, SA 5099</div>
    </div>
  </footer>
  <svg class="contact-tab" viewBox="0 0 680 48" aria-hidden="true"><path d="M0 48 L22 8 Q26 2 34 2 L646 2 Q654 2 658 8 L680 48 Z" fill="var(--green)"/></svg>
  <div class="contact-tab-label">CONTACT US FOR MORE INFORMATION</div>
</main>
</body>
</html>
```